Stationery Design Project

Require letterhead/stationery design based on new logo (see attached).

Would prefer it kept simple but strong and effective.

Target Market(s)

Clients and building developers. Residential/consumer and corporate clientele.

```html
<!DOCTYPE html>
<html lang="en">
<head>
<meta charset="utf-8">
<title>Kestreline Builds – Letterhead</title>
<link href="https://fonts.googleapis.com/css2?family=Marcellus&family=Open+Sans:wght@400;600&display=swap" rel="stylesheet">
<style>
  :root {
    --backdrop: #e6e7e9;
    --paper: #ffffff;
    --ink: #1c1c1c;
    --band: #1a1a1a;
    --accent: #2aa7df;
    --logo-text: #d9dbdd;
    --muted: #3a3a3a;
  }
  * { box-sizing: border-box; margin: 0; padding: 0; }
  html, body {
    width: 1200px; height: 1000px; overflow: hidden;
    background: var(--backdrop);
  }
  .letterhead {
    position: absolute; left: 290px; top: 60px;
    width: 620px; height: 880px;
    background: var(--paper);
    box-shadow: 0 2px 10px rgba(0,0,0,0.12);
  }
  .brand-block {
    position: absolute; left: 56px; top: 52px;
    width: 150px; height: 116px;
    background: var(--band);
    display: flex; flex-direction: column; align-items: center; justify-content: center; gap: 12px;
  }
  .brand-mark {
    width: 30px; height: 30px; background: var(--accent);
  }
  .brand-name {
    font-family: "Marcellus", serif;
    color: var(--logo-text);
    font-size: 15px; letter-spacing: 1px; text-align: center; line-height: 1.15;
  }
  .sender {
    position: absolute; left: 56px; right: 56px; bottom: 92px;
    color: var(--ink);
  }
  .sender-name {
    font-family: "Marcellus", serif;
    font-size: 14px; letter-spacing: 0.6px; text-align: right; margin-bottom: 7px;
  }
  .sender-name .role {
    font-family: "Open Sans", sans-serif; font-weight: 600; font-size: 12px; letter-spacing: 0;
  }
  .contact-row {
    display: flex; justify-content: space-between; align-items: center;
    font-family: "Open Sans", sans-serif; font-size: 11px; color: var(--muted);
    margin-bottom: 7px;
  }
  .contact-item { display: flex; align-items: center; gap: 5px; }
  .contact-item svg { width: 11px; height: 11px; fill: none; stroke: var(--accent); stroke-width: 1.8; }
  .contact-item .filled { fill: var(--accent); stroke: none; }
  .address {
    font-family: "Open Sans", sans-serif; font-weight: 600; font-size: 11px; color: var(--ink);
  }
  .address .company {
    font-family: "Marcellus", serif; font-weight: 400; font-size: 12px; letter-spacing: 0.5px;
  }
  .footer-band {
    position: absolute; left: 0; right: 0; bottom: 50px;
    height: 24px; background: var(--band);
  }
</style>
</head>
<body>
  <main class="letterhead">
    <div class="brand-block">
      <span class="brand-mark"></span>
      <span class="brand-name">KESTRELINE<br>BUILDS</span>
    </div>

    <section class="sender">
      <p class="sender-name">DANIEL HARTLEY - <span class="role">Director</span></p>
      <div class="contact-row">
        <span class="contact-item">
          <svg viewBox="0 0 12 12"><rect x="3" y="1" width="6" height="10" rx="1"/></svg>
          0298765413
        </span>
        <span class="contact-item">
          <svg viewBox="0 0 12 12"><rect class="filled" x="1" y="2.5" width="10" height="7" rx="1"/><path d="M1.5 3 L6 7 L10.5 3" stroke="#fff" stroke-width="1.2"/></svg>
          daniel.h@kestreline.com.au
        </span>
        <span class="contact-item">
          <svg viewBox="0 0 12 12"><circle cx="6" cy="6" r="4.6"/><path d="M1.4 6 H10.6 M6 1.4 C3.8 4 3.8 8 6 10.6 M6 1.4 C8.2 4 8.2 8 6 10.6" stroke-width="1"/></svg>
          www.kestrelinebuilds.com.au
        </span>
      </div>
      <p class="address"><span class="company">KESTRELINE BUILDS,</span> Suite 508, Harbour Lane, Sydney, NSW 2000</p>
    </section>

    <div class="footer-band"></div>
  </main>
</body>
</html>
```